Hollowmere Farm Promotional Leaflet

The team at Hollowmere Farm can help with every aspect of managing and enhancing your home from housekeeping and professional cleaning, laundry and ironing to providing chic and contemporary flower arrangements and even food for your pets!We take pride in providing high-end, consistent and reliable professional services bespoke to you. Whether you are a busy professional working long hours, a stay-at home parent or retired; having professional help in the home gives you time to spend on the things you enjoy.We are providing a very upmarket, highly professional service and need an A5 promotional leaflet to be designed. Please refer to www.hollowmerefarm-example.co.uk and see the section on 'Home Management'The leaflet should incorporate the Hollowmere Farm logo without the 'tipi', and any suitable photography images used on the home page of the website or the 'home management' section.

Target Market(s)

high-end, affluent owners of luxury homes

Industry/Entity Type

Farm

Contact Information for Business Card

The business card design needs to be suitable for use across all of Hollowmere Farm businesses, specifically:
Hollowmere Farm Home Management - otherwise known as Hollowmere Farm @ Home (this uses the typographical logo
Hollowmere Farm Weddings & Events - this uses the 'tipi' logo

Requirements
Must have
• Design in keeping with the look and feel of the logo and website design
• www.hollowmerefarm-example.co.uk

```html
<!DOCTYPE html>
<html lang="en">
<head>
<meta charset="utf-8">
<title>Hollowmere Farm Home Management – Leaflet</title>
<link rel="stylesheet" href="https://fonts.googleapis.com/css2?family=Cinzel:wght@400;500&family=Open+Sans:wght@300;400&display=swap">
<style>
  :root {
    --page-bg: #efe8de;
    --pink-deep: #e02c78;
    --pink-panel: #e23a82;
    --pink-soft: #df5899;
    --pink-edge: #e35c9f;
    --pink-text: #e0307c;
    --gold: #d3a15c;
    --orange: #c98943;
    --white: #ffffff;
  }
  * { box-sizing: border-box; margin: 0; padding: 0; }
  html, body {
    width: 1200px; height: 1200px; overflow: hidden;
    background: var(--page-bg);
  }
  .leaflet {
    position: absolute; left: 235px; top: 84px;
    width: 730px; height: 1031px;
    background: var(--pink-deep);
    overflow: hidden;
    box-shadow: 0 12px 30px rgba(0,0,0,.18);
  }
  .block { position: absolute; }

  /* top section */
  .pattern-top {
    left: 380px; top: 0; width: 350px; height: 460px;
    background: linear-gradient(135deg, #fbf2e6 0%, #efcf9f 45%, #fdf6ec 70%, #e9c48f 100%);
  }
  .hero-photo {
    left: 36px; top: 54px; width: 344px; height: 406px;
    background: linear-gradient(160deg, #5a4b40 0%, #8d7c6b 40%, #b7a895 65%, #6a5a4c 100%);
  }
  .hero-title {
    left: 82px; top: 92px; width: 300px;
    font-family: "Cinzel", serif; font-weight: 400;
    font-size: 35px; line-height: 45px; color: var(--white);
    letter-spacing: .5px;
  }
  .hero-rule {
    left: 82px; top: 231px; width: 268px; height: 1.5px; background: var(--gold);
  }
  .services-panel {
    left: 380px; top: 54px; width: 313px; height: 406px;
    background: var(--pink-panel);
    border-bottom-left-radius: 40px;
    padding: 42px 44px 0 14px;
    font-family: "Open Sans", sans-serif; font-weight: 400;
    font-size: 15.5px; line-height: 22.4px; color: var(--white);
  }
  .services-intro .line { display: block; text-align: justify; text-align-last: justify; white-space: nowrap; }
  .services-intro .line.first { padding-left: 16px; }
  .services-intro .line.last { text-align-last: left; }
  .services-list { list-style: none; padding-left: 16px; white-space: nowrap; }
  .services-list li::before { content: "• "; }

  /* quote band */
  .band-left { left: 0; top: 460px; width: 36px; height: 113px; background: var(--pink-soft); }
  .band-right { left: 693px; top: 460px; width: 37px; height: 113px; background: var(--pink-deep); }
  .quote-band {
    left: 36px; top: 460px; width: 657px; height: 113px;
    background: #f7f5f5;
  }
  .quote-rule {
    left: 248px; top: 470px; width: 262px; height: 1.5px; background: var(--gold);
  }
  .quote {
    left: 36px; top: 477px; width: 657px;
    font-family: "Cinzel", serif; font-size: 14.5px; line-height: 18.8px;
    color: var(--pink-text); text-align: center; letter-spacing: .2px;
  }

  /* promises section */
  .pattern-side {
    left: 0; top: 573px; width: 36px; height: 210px;
    background: linear-gradient(180deg, #f8e9d4, #e3b680, #f8ecdb);
  }
  .promises-panel {
    left: 36px; top: 573px; width: 344px; height: 210px;
    background: var(--pink-soft);
    border-top-right-radius: 40px;
    padding: 14px 14px 0 47px;
    font-family: "Open Sans", sans-serif; font-weight: 400;
    font-size: 15.5px; line-height: 22.4px; color: var(--white);
  }
  .promises-panel ul { list-style: none; white-space: nowrap; }
  .promises-panel li::before { content: "• "; }
  .lifestyle-photo {
    left: 380px; top: 573px; width: 313px; height: 210px;
    background: linear-gradient(180deg, #e9e6e2 0%, #cfc9c2 45%, #24305a 70%, #1b2548 100%);
  }
  .promises-edge { left: 693px; top: 573px; width: 37px; height: 210px; background: var(--pink-edge); }

  /* contact section */
  .contact-base { left: 0; top: 783px; width: 730px; height: 248px; background: var(--orange); }
  .contact-photo {
    left: 36px; top: 783px; width: 344px; height: 202px;
    background: linear-gradient(160deg, #2c2826 0%, #3b3531 50%, #262220 100%);
  }
  .contact-text {
    left: 81px; top: 806px; width: 292px;
    font-family: "Open Sans", sans-serif; font-weight: 300; font-style: normal;
    font-size: 13.4px; line-height: 18.7px; color: var(--white);
  }
  .contact-line { display: flex; align-items: center; gap: 5px; height: 18.7px; white-space: nowrap; }
  .contact-line svg { width: 18px; height: 13px; flex: none; }
  .contact-rule { left: 81px; top: 942px; width: 262px; height: 1.5px; background: var(--gold); }
  .brand-card {
    left: 380px; top: 783px; width: 350px; height: 248px;
    background: linear-gradient(160deg, #f6f6f6, #e9e9e9);
    border-top-left-radius: 36px;
    display: flex; align-items: center; justify-content: center;
    padding-bottom: 14px;
  }
  .brand-name {
    font-family: "Cinzel", serif; font-weight: 500;
    font-size: 30px; color: var(--pink-text); letter-spacing: 1px;
  }
</style>
</head>
<body>
  <main class="leaflet">
    <div class="block pattern-top" role="img" aria-label="Cream and gold swirl pattern"></div>
    <div class="block hero-photo" role="img" aria-label="Photograph of an elegant hallway with chandelier and staircase"></div>
    <h1 class="block hero-title">Hollowmere<br>Farm Home<br>Management</h1>
    <div class="block hero-rule"></div>

    <section class="block services-panel">
      <p class="services-intro">
        <span class="line first">The team @ Hollowmere Farm</span>
        <span class="line">can help with every aspect of</span>
        <span class="line">managing and enhancing your</span>
        <span class="line last">home including:</span>
      </p>
      <ul class="services-list">
        <li>Regular housekeeping<br>and professional cleaning</li>
        <li>Exit cleans</li>
        <li>One-off seasonal/party/<br>building work cleans</li>
        <li>Laundry and ironing</li>
        <li>Chic and contemporary<br>flower arrangements</li>
        <li>Car valeting</li>
        <li>Pet food delivery</li>
        <li>Dry cleaning</li>
      </ul>
    </section>

    <div class="block band-left"></div>
    <div class="block quote-band"></div>
    <div class="block band-right"></div>
    <div class="block quote-rule"></div>
    <blockquote class="block quote">
      “We take pride in providing high-end, consistent and<br>
      reliable professional services bespoke to you.<br>
      Coming home to a beautiful environment and being able to<br>
      relax and enjoy your time is something we all deserve.”
    </blockquote>

    <div class="block pattern-side" role="img" aria-label="Cream and gold swirl pattern"></div>
    <section class="block promises-panel">
      <ul>
        <li>Satisfaction guaranteed</li>
        <li>Professional staff you can trust and<br>rely on</li>
        <li>Competitive rates</li>
        <li>CRB checked and referenced</li>
        <li>Member of the Associated Home<br>Services Federation</li>
        <li>Fully Insured</li>
      </ul>
    </section>
    <div class="block lifestyle-photo" role="img" aria-label="Photograph of a woman relaxing on a navy sofa with her dog"></div>
    <div class="block promises-edge"></div>

    <div class="block contact-base"></div>
    <div class="block contact-photo" role="img" aria-label="Dark-toned photograph of a country house and garden"></div>
    <address class="block contact-text">
      We look after our clients’ homes and holiday<br>lets across South Somerset.<br>
      Contact us to arrange a home visit and<br>quotation:
      <span class="contact-line">
        <svg viewBox="0 0 18 13"><rect x="1" y="1" width="16" height="11" fill="#fff"/><path d="M1 1 L9 7.5 L17 1" fill="none" stroke="#2a2624" stroke-width="1.3"/></svg>
        info@hollowmerefarm-example.co.uk
      </span>
      <span class="contact-line">
        <svg viewBox="0 0 18 13"><path d="M3 0.5 L6 0.5 L7 3.5 L5.5 5 C6.5 7.5 8.5 9.5 11 10.5 L12.5 9 L15.5 10 L15.5 12.5 C8 12.5 3 7.5 3 0.5 Z" fill="#fff"/></svg>
        07700 900123
      </span>
      <span class="contact-line">
        <svg viewBox="0 0 18 13"><circle cx="9" cy="6.5" r="5.8" fill="none" stroke="#fff" stroke-width="1.2"/><path d="M3.2 6.5 H14.8 M9 0.7 C6 3.5 6 9.5 9 12.3 M9 0.7 C12 3.5 12 9.5 9 12.3" fill="none" stroke="#fff" stroke-width="1"/></svg>
        www.hollowmerefarm-example.co.uk
      </span>
    </address>
    <div class="block contact-rule"></div>

    <div class="block brand-card">
      <span class="brand-name">Hollowmere Farm</span>
    </div>
  </main>
</body>
</html>
```